Design some Business Card for shipping company

We need a creative business card designed for a shipping company. All relevant information such as address and phone number can be found on our website. Will need a design for both front and back. The front will container our logo, slogan, contact information etc. The back will have a coupon and some text. check out www.taldovefreight.example for all the information. We need something memorable and unique that will stand out. It needs to a horizontal design. Not vertical.

```html
<!DOCTYPE html>
<html lang="en">
<head>
<meta charset="utf-8">
<title>Taldove Freight – Business Cards</title>
<link rel="stylesheet" href="https://fonts.googleapis.com/css2?family=Open+Sans:wght@300;400;600;700;800&display=swap">
<style>
  :root {
    --bg: #e9e6e1;
    --card-white: #ffffff;
    --pale-green: #e3ecd6;
    --mist-green: #d3e1c2;
    --brand-green: #1f7a3e;
    --deep-green: #17663a;
    --brand-red: #c8202f;
    --ink: #2b2b2b;
    --text-white: #ffffff;
  }
  * { box-sizing: border-box; margin: 0; padding: 0; }
  html, body { width: 1200px; height: 912px; overflow: hidden; }
  body {
    background: var(--bg);
    font-family: "Open Sans", Arial, sans-serif;
    display: flex;
    flex-direction: column;
    align-items: center;
    justify-content: center;
    gap: 40px;
  }
  .card {
    width: 700px;
    height: 400px;
    position: relative;
    overflow: hidden;
    background: var(--card-white);
    box-shadow: 0 4px 14px rgba(0,0,0,0.15);
  }

  /* Brand lockup */
  .brand { display: flex; align-items: center; gap: 14px; }
  .brand-dot {
    width: 58px; height: 58px; border-radius: 50%;
    background: var(--brand-green);
    flex: none;
  }
  .brand-text { display: flex; flex-direction: column; }
  .brand-name {
    font-weight: 800; font-size: 34px; line-height: 1;
    color: var(--brand-green); letter-spacing: 0.5px;
  }
  .brand-slogan {
    font-weight: 700; font-size: 15px; margin-top: 6px;
    color: var(--deep-green);
  }

  /* Card A: brand side */
  .card-brand {
    background: linear-gradient(160deg, var(--card-white) 35%, var(--pale-green) 100%);
  }
  .card-brand .ship-area {
    position: absolute; left: 90px; top: 70px; width: 230px; height: 230px;
    border-radius: 16px;
    background: linear-gradient(180deg, var(--mist-green), var(--pale-green));
    opacity: 0.8;
  }
  .card-brand .swoosh { position: absolute; inset: 0; }
  .card-brand .brand { position: absolute; left: 150px; top: 150px; }
  .card-brand .site {
    position: absolute; left: 222px; top: 250px;
    font-size: 13px; font-weight: 700; letter-spacing: 1px; color: var(--ink);
  }

  /* Card B: contact side */
  .icon-strip {
    position: absolute; left: 0; top: 0; width: 56px; height: 100%;
    display: flex; flex-direction: column; align-items: center;
    padding-top: 46px; gap: 0;
  }
  .icon {
    position: absolute; left: 14px; width: 28px; height: 28px;
  }
  .panel {
    position: absolute; left: 56px; top: 0; width: 330px; height: 100%;
  }
  .panel-name {
    height: 130px; background: var(--brand-red);
    color: var(--text-white);
    padding: 38px 0 0 34px;
  }
  .person-name { font-weight: 300; font-size: 32px; line-height: 1; }
  .person-role { font-weight: 600; font-size: 12px; letter-spacing: 2px; margin-top: 8px; }
  .panel-contact {
    height: 270px; background: var(--brand-green);
    color: var(--text-white);
    padding: 30px 0 0 34px;
    font-size: 15px; line-height: 1.5; font-weight: 400;
  }
  .panel-contact .block { margin-bottom: 14px; }
  .card-contact .brand {
    position: absolute; left: 410px; top: 150px;
    flex-direction: column; align-items: flex-start; gap: 12px;
  }
  .card-contact .brand-name { font-size: 30px; }
  .card-contact .brand-slogan { font-size: 13px; }
</style>
</head>
<body>

  <section class="card card-brand" aria-label="Card brand side">
    <div class="ship-area" role="img" aria-label="Faint cargo ship decoration"></div>
    <svg class="swoosh" viewBox="0 0 700 400" aria-hidden="true">
      <path d="M0 330 C180 260 420 250 700 150" fill="none" stroke="#ffffff" stroke-width="3"/>
      <path d="M0 350 C200 290 440 270 700 175" fill="none" stroke="#ffffff" stroke-width="2"/>
      <path d="M260 0 C360 60 520 70 700 40" fill="none" stroke="#eef3e7" stroke-width="30"/>
    </svg>
    <div class="brand">
      <span class="brand-dot"></span>
      <div class="brand-text">
        <span class="brand-name">Taldove Freight</span>
        <span class="brand-slogan">Secure Affordable Shipping to Kenya</span>
      </div>
    </div>
    <p class="site">WWW.TALDOVEFREIGHT.EXAMPLE</p>
  </section>

  <section class="card card-contact" aria-label="Card contact side">
    <svg class="icon" style="top:40px" viewBox="0 0 28 28" aria-label="Person">
      <circle cx="14" cy="14" r="13" fill="var(--brand-red)"/>
      <circle cx="14" cy="11" r="4" fill="#fff"/>
      <path d="M7 21 C8 15 20 15 21 21 Z" fill="#fff"/>
    </svg>
    <svg class="icon" style="top:175px" viewBox="0 0 28 28" aria-label="Location">
      <circle cx="14" cy="14" r="13" fill="var(--brand-green)"/>
      <path d="M14 6 C10 6 8 9 8 12 C8 16 14 22 14 22 C14 22 20 16 20 12 C20 9 18 6 14 6 Z" fill="#fff"/>
      <circle cx="14" cy="12" r="2.2" fill="var(--brand-green)"/>
    </svg>
    <svg class="icon" style="top:262px" viewBox="0 0 28 28" aria-label="Phone">
      <circle cx="14" cy="14" r="13" fill="var(--brand-green)"/>
      <path d="M9 7 L12 7 L13 11 L11 12.5 C12 15 13 16 15.5 17 L17 15 L21 16 L21 19 C21 20 20 21 19 21 C12 20 8 16 7 9 C7 8 8 7 9 7 Z" fill="#fff"/>
    </svg>
    <svg class="icon" style="top:345px" viewBox="0 0 28 28" aria-label="Website">
      <circle cx="14" cy="14" r="13" fill="var(--brand-green)"/>
      <circle cx="14" cy="14" r="7" fill="none" stroke="#fff" stroke-width="1.6"/>
      <ellipse cx="14" cy="14" rx="3" ry="7" fill="none" stroke="#fff" stroke-width="1.4"/>
      <line x1="7" y1="14" x2="21" y2="14" stroke="#fff" stroke-width="1.4"/>
    </svg>

    <div class="panel">
      <div class="panel-name">
        <p class="person-name">Daniel REYES</p>
        <p class="person-role">PROJECT MANAGER</p>
      </div>
      <div class="panel-contact">
        <div class="block">
          Taldove freight<br>
          1480 Harbor Crest Ave<br>
          Suite #118<br>
          Northport WA 98010
        </div>
        <div class="block">
          USA &nbsp;+1 555 014 2290<br>
          Kenya &nbsp;+254 700 555 018<br>
          0700 555 018
        </div>
        <div class="block">www.taldovefreight.example</div>
      </div>
    </div>

    <div class="brand">
      <span class="brand-dot"></span>
      <div class="brand-text">
        <span class="brand-name">Taldove Freight</span>
        <span class="brand-slogan">Secure Affordable Shipping to Kenya</span>
      </div>
    </div>
  </section>

</body>
</html>
```